Desert Basin Company Brochure

**** UPDATE 2-8-2014 ****

Size should be 11" X 17" or larger (tri or bi fold).

We're going to let the contest run it's full duration to allow for more time spent on designs.

No black backgrounds.

Consideration should be given to having the text be easy to read and in a nice, organized format.

*****************************

We're looking for an eye-catching, colorful brochure that will explain what we do, who we are... and what sets us apart from the competition.

Our company provides swimming pool service, repair, and custom renovations throughout the Phoenix, Arizona metropolitan area. These brochures will be hand-delivered to each prospective customer we visit.

The brochure will include images of our work, product logos, and a unique design that separates our company apart from the rest.

The brochure should be tri-fold. Although, if a designer wants to (or has better ideas) for a different lay-out, then we're open to seeing what can be done.

Colors we like: Blue, White, Silver, Copper, Green (accent color)

We like designs that are unique/different. Professional. Creative. Sleek. Sexy. Custom. We don't want the brochure to be "pretentious". We'd like for these brochures to leave a lasting impression with our prospective clients... and hopefully earn us more business.

We don't want the brochure to be too wordy, however if the designer feels we need to cut back (or add), let us know.

Our motto is "Every Ripple Counts Twice".

You can view some of our projects, and what we're about either at our website (brightwaveaqua.example), Chatterbook (www.facebook/brightwaveaqua), or Searchly+ (https://plus.google.com/+Brightwaveaqua). Thank you!

- Print-

(Front) Logo

Service - Repair - Renovation
555-731-4409
brightwaveaqua.example
service@brightwaveaqua.example
Like Us On Chatterbook! Chatterbook LOGO
Searchly Plus LOGO

(Body) Why Choose Us?

Thank you for the opportunity for our company to become your pool service provider!

We’re committed to providing the best customer service possible! At the end of the day you want your pool to be clean, clear, operational, and for your service provider to be available when you need them!

We’re licensed with the Westland Board Of Tradesmen, Bonded, and Fully Insured.
A+ reviews with the Honest Trade Council, Marla’s Picks, Wombit, Vyn, Chatterbook, and Searchly!
All technicians are employees... not sub-contractors! Our employees are hard working, dependable, professional, and expected to follow our strict protocol for servicing your pool.
Flat-fee service rates! Any additional equipment repairs, maintenance, or chemical implementations are directly authorized by you!
No contracts! Our Service Level Agreement Form allows you to select your desired level of authorization for equipment repairs, filter maintenance, and extra chemical implementation programs.
Our uniformed technicians arrive in distinctive, clean GPS-tracked company trucks.
We leave detailed service slips after each service visit. In addition, all service visit information is electronically recorded and stored.
Easy, online account management to view and pay invoices or authorize estimates.
Invoices, estimates, questions, pictures, and video are communicated via e-mail!
Free service calls to diagnose equipment issues outside of our normal service.
10% Service Client Discount for all repairs and replacement items.
Brightwave Aqua knows the importance of communication! We’re available by phone, email, or text all days of the week.

(Body) Our Methodology

We believe in 5 important factors in maintaining a clean, clear, and operational pool...

Good, Clean Water! Our local water supply contains high amounts of minerals. Pool chemicals add to this problem in a short amount of time. Our philosophy is to use the least amount of chemicals possible to achieve optimal water balance.
Efficient Water Flow! The invention of variable-speed pumps has enabled the ability to "dial in" proper water flow... while driving down energy costs.
Proper Filtration! Today’s high-capacity cartridge filters provide great filtration, save on wasted water from backwashing sand filters, and eliminate the need for water flow-restricting backwash valves.
Functioning Cleaning System! Having a working automatic cleaning system is vital in keeping the pool surface clean of debris and dirt... and free of staining.
A Dependable And Professional Pool Maintenance Technician! Our job is to not only oversee all of the items listed above... but to make sure your pool is in the best condition possible!

(Body) Equipment Repair & Installation

We’re educated on all phases of swimming pool equipment repair and installation... with a focus on energy-efficiency and optimum performance!

We’re an KTV & MWE Authorized Installer of variable-speed pool pumps. KTV & MWE trust us to properly install and calibrate all variable-speed pumps. We've been equipped to handle the new industry standards on variable-speed pumps since Arizona law went into effect January 1st, 2011.
We’re experts at acid washes and erasing the mineral build-up off of waterlines. All work is done in-house with our customized cleaning rig and trailer.
Heating systems. New efficiency standards have made installation and operation more affordable than ever.
Remote control automation systems. Technology now allows the user to easily view and control their entire pool system via a remote home computer, tablet, or phone!
Brilliant, color-changing LED lighting for pools and spas! The benefits of LED include brighter and broader displays... while lasting much longer than your typical light bulbs.
Salt systems provide a soft-water experience! In addition to the benefit of better feeling water, salt systems generate plenty of chlorine to keep your pool sanitized.

(Body) About Us

A native to Phoenix, Dorian Kessel founded Brightwave Aqua in 2000. Our company was built from the ground up by way of hard work, word of mouth, and determination. Our company will always remain firmly grounded, and continue to develop systems that put our customers first!

Our philosophy is to treat every pool as if it were our own, run an efficient and organized business, and care for our employees.

Brightwave Aqua is a yearly, proud contributor to the Saguaro Youth Medical Center Splash Smart Day. Please educate and watch all children around water... every accident can be avoided.

(Back) Contact Us
Logos To Use, Files Uploaded: Marla’s Picks, HTC, Hydrova, Searchly+, Chatterbook, KTV/MWE logo, Saguaro Youth Medical Center

Office: 555-731-4409 | Fax: 555-731-4413 | Email: service@brightwaveaqua.example
brightwaveaqua.example

Office / Warehouse Location
41276 East Cholla Street, Suite 8
Phoenix, Arizona 85999
(NW of Cholla Street & Ironwood Mesa Road)

AZ ROC: 731502, 731503, 731504, 864017

Target Market(s)

We target a market of pool owners, which typically have more disposable income.

30 - 75 years old.

Our clients range from first-time home buyers, self-employed, business professionals, doctors, landlords, thousandaires, millionaires.

Industry/Entity Type

Pool Service

Font styles to use
Serif

Colors
0355a3
cfdfed
ffffff
3176b5
eaf1f7

Requirements
Must have
• Must use provided images. We've included a few pool pictures, and will let you decide which ones to incorporate throughout the brochure.

Logos Used:
Brightwave Aqua
Hydrova
HTC
Marla's Picks
KTV
MWE
Saguaro Youth Medical Center
Searchly+
Chatterbook

Image pic of some of our trucks.

Nice to have
• Equipment images worked in.
Should not have
• Cartoonish fonts or design. No "Love" hearts!!

```html
<!DOCTYPE html>
<html lang="en">
<head>
<meta charset="utf-8">
<title>Brightwave Aqua Brochure</title>
<link rel="stylesheet" href="https://fonts.googleapis.com/css2?family=Open+Sans:wght@300;400;600;700;800&display=swap">
<style>
:root{
  --blue-deep:#0355a3;
  --blue-mid:#3176b5;
  --blue-dark:#06336b;
  --blue-ice:#cfdfed;
  --blue-mist:#eaf1f7;
  --white:#ffffff;
  --silver:#d9dde2;
  --ink:#1f3b5c;
  --stage:#b9bcbf;
}
*{box-sizing:border-box;margin:0;padding:0}
html,body{width:900px;height:1200px;overflow:hidden}
body{background:var(--stage);font-family:"Open Sans",Arial,sans-serif;position:relative;color:var(--ink)}
.spread{position:absolute;left:20px;width:860px;height:556px;display:flex;box-shadow:0 4px 14px rgba(0,0,0,.25)}
.spread--outside{top:30px}
.spread--inside{top:614px}
.panel{position:relative;width:430px;height:556px;overflow:hidden}
.photo{position:absolute}
.tick-list{list-style:none}
.tick-list li{position:relative;padding-left:11px;margin-bottom:3px}
.tick-list li::before{content:"✔";position:absolute;left:0;top:0;color:#7fd0ff;font-size:7px}
.brand{font-weight:800;color:var(--blue-deep);display:flex;align-items:center;gap:6px}
.brand-dot{width:16px;height:16px;border-radius:50%;background:var(--blue-mid);flex:none}

/* back panel */
.back{background:var(--white)}
.back-header{position:absolute;left:0;top:0;width:430px;height:38px;background:linear-gradient(90deg,var(--blue-deep),var(--blue-mid));border-bottom-right-radius:60px}
.back-header h2{color:var(--white);font-weight:300;font-size:17px;padding:9px 0 0 18px}
.back-header h2 b{font-weight:700}
.back-intro{position:absolute;left:18px;top:46px;width:395px;font-size:7.4px;color:var(--blue-deep);font-style:italic;line-height:1.35}
.back-list{position:absolute;left:18px;top:72px;width:395px;font-size:6.2px;line-height:1.35;color:var(--ink)}
.back-list li::before{color:var(--blue-mid)}
.back-list b{color:var(--blue-deep)}
.about-title{position:absolute;left:18px;top:196px;font-size:17px;font-weight:700;color:var(--blue-deep)}
.about-box{position:absolute;left:14px;top:220px;width:402px;padding:6px 10px;border-radius:10px;background:var(--blue-mist);font-size:6.2px;line-height:1.4}
.about-box p+p{margin-top:4px}
.partners{position:absolute;left:18px;top:300px;width:395px;height:60px;display:flex;align-items:center;justify-content:space-between}
.partner{background:var(--blue-ice);border:1px solid #b7cbe0}
.partner--round{width:44px;height:44px;border-radius:50%}
.partner--wide{width:64px;height:26px;border-radius:4px}
.partner--square{width:40px;height:40px;border-radius:4px}
.back-footer{position:absolute;left:0;top:372px;width:430px;height:184px;background:linear-gradient(180deg,var(--blue-mid),var(--blue-deep) 40%,var(--blue-dark))}
.back-footer .brand{position:absolute;left:20px;top:70px;font-size:19px;color:var(--white)}
.back-footer .brand-dot{background:var(--blue-ice)}
.back-footer .tagline{position:absolute;left:42px;top:96px;font-size:7px;color:var(--blue-ice)}
.contact{position:absolute;left:226px;top:40px;font-size:7px;line-height:1.5;color:var(--white);border-left:1px solid rgba(255,255,255,.5);padding-left:10px}
.contact li{list-style:none;display:flex;align-items:center;gap:5px}
.contact svg{flex:none}
.social-row{display:flex;gap:6px;margin-top:6px}
.social{display:flex;align-items:center;gap:4px;font-weight:600;font-size:7px;color:var(--white)}
.social i{width:9px;height:9px;background:var(--white);opacity:.85;display:block}

/* front panel */
.front{background:linear-gradient(180deg,var(--blue-mid),var(--blue-deep) 55%,var(--blue-dark))}
.front .photo{left:0;top:60px;width:430px;height:240px;background:linear-gradient(160deg,#7fa07c 0%,#b49f86 35%,#5fb2c9 60%,#1a7fa6 100%);clip-path:ellipse(78% 100% at 78% 0%)}
.front .brand{position:absolute;right:26px;top:40px;font-size:22px}
.front .tagline{position:absolute;right:26px;top:68px;font-size:8px;font-weight:600;color:var(--blue-deep)}
.services{position:absolute;left:26px;top:312px;font-size:22px;font-weight:300;color:var(--white);letter-spacing:.3px}
.front-bar{position:absolute;left:0;top:354px;width:430px;height:36px;background:linear-gradient(90deg,var(--white),var(--blue-mist));display:flex;align-items:center;padding-left:26px;gap:10px;font-weight:700;color:var(--blue-dark)}
.front-bar .url{font-size:11px}
.front-bar .phone{font-size:14px;border-left:2px solid var(--blue-mid);padding-left:10px}
.front-bar .social{color:var(--blue-deep);border-left:2px solid var(--blue-mid);padding-left:8px}
.front-bar .social i{background:var(--blue-mid)}

/* inside */
.inside-left,.inside-right{background:linear-gradient(180deg,var(--blue-mid),var(--blue-deep) 40%,var(--blue-dark))}
.inside-left .photo--hero{left:0;top:0;width:430px;height:170px;background:linear-gradient(180deg,#9cc7e3 0%,#c9b79c 45%,#2f9fc0 70%,#0e6a95 100%);clip-path:polygon(0 0,100% 0,100% 70%,0 100%)}
.inside-right .photo--hero{left:0;top:0;width:430px;height:175px;background:linear-gradient(180deg,#a9b08e 0%,#c8ab86 40%,#3a94b0 70%,#0f5f86 100%);clip-path:polygon(0 0,100% 0,100% 82%,0 58%)}
.section-title{position:absolute;color:var(--white);font-size:20px;font-weight:300}
.section-title b{font-weight:700}
.lead{position:absolute;color:var(--white);font-weight:700;font-size:8px;line-height:1.3}
.body-copy{position:absolute;color:var(--white);font-size:6.1px;line-height:1.35}
.circle{position:absolute;border-radius:50%;border:4px solid var(--white);box-shadow:0 2px 6px rgba(0,0,0,.35)}
.inside-bar{position:absolute;height:34px;background:linear-gradient(90deg,var(--white),var(--blue-mist));display:flex;align-items:center;gap:12px}
.inside-bar .phone{font-size:15px;font-weight:700;color:var(--blue-dark)}
.inside-bar .brand{font-size:14px}
.trucks{position:absolute;left:232px;top:420px;width:150px;height:58px;border:3px solid var(--white);border-radius:4px;background:linear-gradient(180deg,#bcd3e6,#8da7bd 60%,#6b7c8a)}
.fold{position:absolute;left:430px;top:0;width:1px;height:556px;background:rgba(0,0,0,.12)}
</style>
</head>
<body>

<!-- Outside spread: back cover + front cover -->
<section class="spread spread--outside">
  <article class="panel back">
    <header class="back-header"><h2>Equipment <b>Repair &amp; Installation</b></h2></header>
    <p class="back-intro">We’re educated on all phases of swimming pool equipment repair and installation... with a focus on energy-efficiency and optimum performance!</p>
    <ul class="tick-list back-list">
      <li><b>We’re an KTV &amp; MWE Authorized Installer of variable-speed pool pumps.</b> KTV &amp; MWE trust us to properly install and calibrate all variable-speed pumps. We've been equipped to handle the new industry standards on variable-speed pumps since Arizona law went into effect January 1st, 2011.</li>
      <li><b>We’re experts at acid washes and erasing the mineral build-up off of waterlines.</b> All work is done in-house with our customized cleaning rig and trailer.</li>
      <li><b>Heating systems.</b> New efficiency standards have made installation and operation more affordable than ever.</li>
      <li><b>Remote control automation systems.</b> Technology now allows the user to easily view and control their entire pool system via a remote home computer, tablet, or phone!</li>
      <li><b>Brilliant, color-changing LED lighting for pools and spas!</b> The benefits of LED include brighter and broader displays... while lasting much longer than your typical light bulbs.</li>
      <li><b>Salt systems provide a soft-water experience!</b> In addition to the benefit of better feeling water, salt systems generate plenty of chlorine to keep your pool sanitized.</li>
    </ul>
    <h2 class="about-title">About Us</h2>
    <div class="about-box">
      <p>A native to Phoenix, Dorian Kessel founded Brightwave Aqua in 2000. Our company was built from the ground up by way of hard work, word of mouth, and determination. Our company will always remain firmly grounded, and continue to develop systems that put our customers first!</p>
      <p>Our philosophy is to treat every pool as if it were our own, run an efficient and organized business, and care for our employees.</p>
      <p>Brightwave Aqua is a yearly, proud contributor to the Saguaro Youth Medical Center Splash Smart Day. Please educate and watch all children around water... every accident can be avoided.</p>
    </div>
    <div class="partners" aria-label="Partner and listing badges">
      <span class="partner partner--round" role="img" aria-label="Marla's Picks badge"></span>
      <span class="partner partner--wide" role="img" aria-label="KTV and Hydrova badges"></span>
      <span class="partner partner--wide" role="img" aria-label="MWE and Saguaro Youth Medical Center badges"></span>
      <span class="partner partner--square" role="img" aria-label="HTC accreditation badge"></span>
    </div>
    <footer class="back-footer">
      <div class="brand"><span class="brand-dot"></span>brightwaveaqua</div>
      <p class="tagline">Every Ripple Counts Twice</p>
      <ul class="contact">
        <li><svg width="8" height="8" viewBox="0 0 10 10"><path d="M5 0a3.5 3.5 0 0 0-3.5 3.5C1.5 6 5 10 5 10s3.5-4 3.5-6.5A3.5 3.5 0 0 0 5 0z" fill="#fff"/></svg>Warehouse Location: 41276 East Cholla Street, Suite 8</li>
        <li style="padding-left:13px">Phoenix, Arizona 85999</li>
        <li style="padding-left:13px">(NW of Cholla Street &amp; Ironwood Mesa Road)</li>
        <li><svg width="8" height="8" viewBox="0 0 10 10"><path d="M2 0l2 2.5-1 1.5c.8 1.5 1.5 2.2 3 3l1.5-1L10 8 8.5 10C4 9 1 6 0 1.5z" fill="#fff"/></svg>555-731-4409</li>
        <li><svg width="8" height="8" viewBox="0 0 10 10"><rect x="1" y="2" width="8" height="6" fill="#fff"/></svg>555-731-4413</li>
        <li><svg width="8" height="8" viewBox="0 0 10 10"><rect x="0.5" y="2" width="9" height="6" fill="none" stroke="#fff"/><path d="M.5 2 5 6 9.5 2" fill="none" stroke="#fff"/></svg>service@brightwaveaqua.example</li>
        <li><svg width="8" height="8" viewBox="0 0 10 10"><circle cx="5" cy="5" r="4.3" fill="none" stroke="#fff"/></svg>www.brightwaveaqua.example</li>
        <li class="social-row"><span class="social"><i></i>Chatterbook</span><span class="social"><i></i>Searchly+</span></li>
      </ul>
    </footer>
  </article>

  <article class="panel front">
    <svg width="430" height="556" style="position:absolute;left:0;top:0" aria-hidden="true">
      <path d="M0 0H430V300C340 250 220 230 120 260 70 275 30 295 0 310Z" fill="#eef2f6"/>
      <path d="M0 300C80 262 200 250 300 270 360 282 400 300 430 320V340C360 300 220 280 120 296 60 306 20 320 0 330Z" fill="#cfdfed" opacity=".35"/>
    </svg>
    <div class="photo" role="img" aria-label="Photo of a rock-waterfall swimming pool with palm trees"></div>
    <div class="brand"><span class="brand-dot"></span>brightwaveaqua</div>
    <p class="tagline">Every Ripple Counts Twice</p>
    <p class="services">• Service • Repair • Renovation</p>
    <div class="front-bar">
      <span class="url">www.brightwaveaqua.example</span>
      <span class="phone">555-731-4409</span>
      <span class="social"><i></i>Chatterbook</span>
      <span class="social"><i></i>Searchly+</span>
    </div>
  </article>
  <span class="fold"></span>
</section>

<!-- Inside spread -->
<section class="spread spread--inside">
  <article class="panel inside-left">
    <div class="photo photo--hero" role="img" aria-label="Photo of a tiled pool and patio with potted plant"></div>
    <h2 class="section-title" style="left:20px;top:168px">Why <b>Choose Us?</b></h2>
    <p class="lead" style="left:20px;top:196px;width:270px">Thank you for the opportunity for our company to become your pool service provider!</p>
    <div class="body-copy" style="left:20px;top:218px;width:272px">
      <p style="margin-bottom:3px">We’re committed to providing the best customer service possible! At the end of the day you want your pool to be clean, clear, operational, and for your service provider to be available when you need them!</p>
      <ul class="tick-list">
        <li>We’re licensed with the Westland Board Of Tradesmen, Bonded, and Fully Insured.</li>
        <li>A+ reviews with the Honest Trade Council, Marla’s Picks, Wombit, Vyn, Chatterbook, and Searchly!</li>
        <li>All technicians are employees... not sub-contractors! Our employees are hard working, dependable, professional, and expected to follow our strict protocol for servicing your pool.</li>
        <li>Flat-fee service rates! Any additional equipment repairs, maintenance, or chemical implementations are directly authorized by you!</li>
        <li>No contracts! Our Service Level Agreement Form allows you to select your desired level of authorization for equipment repairs, filter maintenance, and extra chemical implementation programs.</li>
        <li>Our uniformed technicians arrive in distinctive, clean GPS-tracked company trucks.</li>
        <li>We leave detailed service slips after each service visit. In addition, all service visit information is electronically recorded and stored.</li>
        <li>Easy, online account management to view and pay invoices or authorize estimates.</li>
        <li>Invoices, estimates, questions, pictures, and video are communicated via e-mail!</li>
        <li>Free service calls to diagnose equipment issues outside of our normal service.</li>
        <li>10% Service Client Discount for all repairs and replacement items.</li>
        <li>Brightwave Aqua knows the importance of communication! We’re available by phone, email, or text all days of the week.</li>
      </ul>
    </div>
    <div class="circle" role="img" aria-label="Photo of a technician cleaning a spa" style="left:312px;top:196px;width:96px;height:96px;background:radial-gradient(circle at 40% 40%,#8fb07a,#4a8aa6 70%,#2a5f7a)"></div>
    <div class="circle" role="img" aria-label="Photo of pool equipment and stone water feature" style="left:312px;top:305px;width:96px;height:96px;background:radial-gradient(circle at 50% 40%,#c9b49a,#7a8c9a 60%,#3a5d78)"></div>
    <div class="inside-bar" style="left:0;top:500px;width:430px;padding-left:20px">
      <div class="brand"><span class="brand-dot"></span>brightwaveaqua</div>
      <span class="phone" style="margin-left:20px">555-731-4409</span>
    </div>
  </article>

  <article class="panel inside-right">
    <div class="photo photo--hero" role="img" aria-label="Photo of a freeform pool with rock waterfall and deck"></div>
    <h2 class="section-title" style="left:22px;top:178px">Our <b>Methodology</b></h2>
    <p class="lead" style="left:22px;top:206px;width:210px">We believe in 5 important factors in maintaining a clean, clear, and operational pool...</p>
    <div class="body-copy" style="left:22px;top:234px;width:205px">
      <ul class="tick-list">
        <li><b>Good, Clean Water!</b> Our local water supply contains high amounts of minerals. Pool chemicals add to this problem in a short amount of time. Our philosophy is to use the least amount of chemicals possible to achieve optimal water balance.</li>
        <li><b>Efficient Water Flow!</b> The invention of variable-speed pumps has enabled the ability to "dial in" proper water flow... while driving down energy costs.</li>
        <li><b>Proper Filtration!</b> Today’s high-capacity cartridge filters provide great filtration, save on wasted water from backwashing sand filters, and eliminate the need for water flow-restricting backwash valves.</li>
        <li><b>Functioning Cleaning System!</b> Having a working automatic cleaning system is vital in keeping the pool surface clean of debris and dirt... and free of staining.</li>
        <li><b>A Dependable And Professional Pool Maintenance Technician!</b> Our job is to not only oversee all of the items listed above... but to make sure your pool is in the best condition possible!</li>
      </ul>
    </div>
    <div class="circle" role="img" aria-label="Photo of a pebble-finish pool" style="left:300px;top:176px;width:92px;height:92px;background:radial-gradient(circle at 50% 45%,#3d8fae,#6f8f8a 65%,#b9a98f)"></div>
    <div class="circle" role="img" aria-label="Photo of a pool overlooking the desert" style="left:318px;top:282px;width:92px;height:92px;background:radial-gradient(circle at 50% 60%,#4aa0bf,#9fb3a8 60%,#c7c2b4)"></div>
    <div class="trucks" role="img" aria-label="Photo of the company service trucks"></div>
    <div class="inside-bar" style="left:232px;top:486px;width:198px;justify-content:flex-end;padding-right:16px">
      <span class="phone">555-731-4409</span>
    </div>
    <div class="brand" style="position:absolute;left:300px;top:452px;font-size:12px;color:var(--white)"><span class="brand-dot" style="width:10px;height:10px;background:var(--blue-ice)"></span>brightwaveaqua</div>
  </article>
  <span class="fold"></span>
</section>

</body>
</html>
```